Corvana Wound Care Business card design

We need a business card designed around our logo which was provided. The logo of preference is the colored. Also the colors and fonts were provided.

Target Market(s)

Our Referral partners are home health agencies.

Industry/Entity Type

Healthcare

Contact Information for Business Card

Name , Phone #, Email , Title

Requirements
Nice to have
• Creativity
Should not have
• basic

```html
<!DOCTYPE html>
<html lang="en">
<head>
<meta charset="utf-8">
<title>Corvana Wound Care — Business Card</title>
<link rel="stylesheet" href="https://fonts.googleapis.com/css2?family=Domine:wght@400;700&display=swap">
<style>
  :root {
    --backdrop: #232325;
    --card: #1f1f24;
    --ink-deep: #0c0c0e;
    --blue-deep: #2a3f9e;
    --blue-mid: #1d5fb8;
    --blue-bright: #1ea0dc;
    --white: #ffffff;
    --divider: #1d4f9e;
  }
  * { margin: 0; padding: 0; box-sizing: border-box; }
  html, body {
    width: 1200px; height: 800px; overflow: hidden;
    background: var(--backdrop);
    font-family: "Domine", Georgia, serif;
  }
  .sheet {
    width: 1200px; height: 800px;
    display: flex; flex-direction: column;
    align-items: center; justify-content: center; gap: 36px;
  }
  .card {
    position: relative;
    width: 620px; height: 354px;
    background: var(--card);
    box-shadow: 0 10px 28px rgba(0,0,0,.55);
    overflow: hidden;
  }

  /* Front */
  .card-front { display: flex; align-items: center; justify-content: center; }
  .front-name {
    color: var(--ink-deep);
    font-weight: 700; font-size: 44px; letter-spacing: .5px;
  }
  .front-name small { display: block; font-size: 13px; letter-spacing: 9px; text-align: right; margin-top: 4px; }

  /* Back */
  .brand {
    position: absolute; left: 44px; top: 118px;
    display: flex; align-items: center; gap: 14px;
  }
  .brand-mark { width: 30px; height: 30px; background: var(--blue-mid); }
  .brand-name {
    color: var(--blue-mid); font-weight: 700; font-size: 38px; line-height: 1;
  }
  .brand-name small { display: block; font-size: 11px; letter-spacing: 8px; margin-top: 8px; text-align: right; }

  .divider {
    position: absolute; left: 318px; top: 56px;
    width: 1px; height: 200px; background: var(--divider);
  }
  .person { position: absolute; left: 352px; top: 54px; }
  .person-name { color: var(--blue-mid); font-weight: 700; font-size: 30px; line-height: 1.1; }
  .person-title { color: var(--white); font-size: 14px; margin-top: 6px; }

  .contacts { position: absolute; left: 352px; top: 156px; list-style: none; }
  .contacts li {
    display: flex; align-items: center; gap: 12px;
    color: var(--white); font-size: 14px; margin-bottom: 10px;
  }
  .contacts svg { width: 16px; height: 16px; flex: none; }

  .address-band {
    position: absolute; left: 0; bottom: 30px;
    width: 100%; height: 40px;
    background: linear-gradient(90deg, var(--blue-deep), var(--blue-mid) 70%, var(--blue-bright));
    display: flex; align-items: center; padding-left: 34px;
    color: var(--white); font-size: 14.5px;
  }
  .address-band::after {
    content: ""; position: absolute; right: 0; top: -16px;
    width: 64px; height: 26px; background: var(--blue-bright);
  }
</style>
</head>
<body>
<main class="sheet">
  <section class="card card-front" aria-label="Card front">
    <p class="front-name">Corvana<small>WOUND CARE</small></p>
  </section>

  <section class="card card-back" aria-label="Card back">
    <div class="brand">
      <span class="brand-mark"></span>
      <p class="brand-name">Corvana<small>WOUND CARE</small></p>
    </div>

    <span class="divider"></span>

    <div class="person">
      <h1 class="person-name">Marta Kovalen</h1>
      <p class="person-title">Founder &amp; CEO</p>
    </div>

    <ul class="contacts">
      <li>
        <svg viewBox="0 0 24 24" fill="none" stroke="#1ea0dc" stroke-width="2.2"><path d="M5 3h4l2 5-3 2a12 12 0 0 0 6 6l2-3 5 2v4a2 2 0 0 1-2 2A18 18 0 0 1 3 5a2 2 0 0 1 2-2z"/></svg>
        +1 555-014-2736
      </li>
      <li>
        <svg viewBox="0 0 24 24" fill="none" stroke="#1ea0dc" stroke-width="2"><circle cx="12" cy="12" r="9"/><path d="M3 12h18M12 3c3 3 3 15 0 18M12 3c-3 3-3 15 0 18"/></svg>
        www.corvanacare.com
      </li>
      <li>
        <svg viewBox="0 0 24 24" fill="none" stroke="#1ea0dc" stroke-width="2"><rect x="3" y="6" width="18" height="13"/><path d="M3 6l9 7 9-7"/></svg>
        info@corvanacare.com
      </li>
    </ul>

    <p class="address-band">2280 Maple Ridge Pkwy. , Alder Falls, GA, United States, 30190</p>
  </section>
</main>
</body>
</html>
```